Freelance Translator in Need of a Business Card

I am a freelance Japanese to English translator. I work in the video game localization industry and do literary translation in my spare time. I would like to have both the English word 'Translator' and the Japanese '翻訳者' in the job title. The final design should evoke trust, openness, and reliability.

Target Market(s)

Video game localization companies
Japanese comic book artists

Industry/Entity Type

Business

Contact Information for Business Card

Daniel Oskerby, Translator
dan.oskerby@fernlowmail.com
velmotranslates.com
twitter: @velmo_tl

Colors

Designer to choose colors to be used in the design.

```html
<!DOCTYPE html>
<html lang="en">
<head>
<meta charset="utf-8">
<title>Daniel Oskerby — Business Card</title>
<link rel="stylesheet" href="https://fonts.googleapis.com/css2?family=Lato:wght@400;700&family=Noto+Sans+JP:wght@400&display=swap">
<style>
  :root {
    --backdrop: #3b3b3b;
    --card: #0b0b0b;
    --ink: #ffffff;
    --ink-soft: #e6e6e6;
  }
  * { margin: 0; padding: 0; box-sizing: border-box; }
  html, body {
    width: 1200px;
    height: 750px;
    overflow: hidden;
    background: var(--backdrop);
  }
  .sheet {
    position: relative;
    width: 1200px;
    height: 750px;
  }
  .card {
    position: absolute;
    left: 366px;
    width: 467px;
    height: 267px;
    background: var(--card);
    color: var(--ink);
    font-family: "Lato", "Helvetica Neue", Arial, sans-serif;
  }
  .card--front { top: 93px; }
  .card--back { top: 406px; }

  /* Front: name mark */
  .mark {
    position: absolute;
    left: 173px;
    top: 72px;
    width: 121px;
    height: 121px;
  }
  .mark__ring {
    position: absolute;
    inset: 0;
    border: 2.5px solid var(--ink);
    border-radius: 50%;
  }
  .mark__name {
    position: absolute;
    left: 50%;
    top: 86px;
    transform: translateX(-50%);
    padding: 2px 6px;
    background: var(--card);
    white-space: nowrap;
    font-size: 16px;
    font-weight: 400;
    letter-spacing: 0.5px;
    color: var(--ink);
    line-height: 20px;
  }

  /* Back: contact block */
  .contact {
    position: absolute;
    left: 280px;
    top: 156px;
  }
  .contact__name {
    font-size: 14.5px;
    font-weight: 400;
    line-height: 18px;
  }
  .contact__role {
    font-size: 12px;
    line-height: 15px;
    color: var(--ink-soft);
  }
  .contact__role-jp {
    font-family: "Noto Sans JP", sans-serif;
    margin-left: 9px;
    font-size: 11.5px;
  }
  .contact__list {
    list-style: none;
    margin-top: 10px;
  }
  .contact__item {
    display: flex;
    align-items: center;
    height: 16px;
    font-size: 12px;
    color: var(--ink-soft);
  }
  .contact__icon {
    width: 9px;
    height: 9px;
    margin-right: 10px;
    flex: none;
  }
</style>
</head>
<body>
<main class="sheet">
  <section class="card card--front" aria-label="Card front">
    <div class="mark">
      <div class="mark__ring"></div>
      <span class="mark__name">DANIEL OSKERBY</span>
    </div>
  </section>

  <section class="card card--back" aria-label="Card back">
    <div class="contact">
      <p class="contact__name">Daniel Oskerby</p>
      <p class="contact__role">Translator<span class="contact__role-jp" lang="ja">翻訳者</span></p>
      <ul class="contact__list">
        <li class="contact__item">
          <svg class="contact__icon" viewBox="0 0 10 8" aria-hidden="true">
            <rect x="0" y="0" width="10" height="8" fill="#e6e6e6"/>
            <path d="M0 0 L5 4.5 L10 0" fill="none" stroke="#0b0b0b" stroke-width="1"/>
          </svg>
          dan.oskerby@fernlowmail.com
        </li>
        <li class="contact__item">
          <svg class="contact__icon" viewBox="0 0 10 10" aria-hidden="true">
            <circle cx="5" cy="5" r="4.4" fill="none" stroke="#e6e6e6" stroke-width="1"/>
            <ellipse cx="5" cy="5" rx="2" ry="4.4" fill="none" stroke="#e6e6e6" stroke-width="0.8"/>
            <line x1="0.6" y1="5" x2="9.4" y2="5" stroke="#e6e6e6" stroke-width="0.8"/>
          </svg>
          velmotranslates.com
        </li>
        <li class="contact__item">
          <svg class="contact__icon" viewBox="0 0 10 10" aria-hidden="true">
            <circle cx="5" cy="5" r="4.5" fill="#e6e6e6"/>
          </svg>
          @velmo_tl
        </li>
      </ul>
    </div>
  </section>
</main>
</body>
</html>
```